We need packaging box design for our solar lights

We need a design for our solar string lights packaging boxes. The final design should communicate an added enjoyment, comfort and beauty when our lights are used to light up warm evening nights in places like backyard, patio restaurant or even family event.

Front and back side of box can be more visual while sides can be used for technical information about the product. There are 2 types of boxes which will have same design - except they need to indicate difference in # of bulbs 10 or 16 . also size of 16 bulb product box is slightly larger so design will need to be slightly adjusted.

Our original logo needs to have "Lumen Nook" text added to it as well.

We put all together in the attachment with some of the examples of photos we like.

Below are more attached files:
1st attachment - general info and samples of photos
Second attachments are photos of our product - they can be adjusted/photoshoped in any way you wish to make the design - or any other acceptable photos you create can be used
Third set of attachments are box templates for 10 and 16 bulbs size box
last are files for logo - choose any you like, edit any colors / text needs to be added/changed to "Lumen Nook " - not go with nook

Target Market(s)

People with yards, patios, restaurants, wedding places... any celebrations or just relaxing during nice warm evening in the beautifully lit place...

Colors

Designer to choose colors to be used in the design.

Requirements
Must have
• indication of bulb numbers
• logo and name Lumen nook
• rest is up to creativity of designer
Nice to have
• some icons

```html
<!DOCTYPE html>
<html lang="en">
<head>
<meta charset="utf-8">
<title>Lumen Nook – Solar Outdoor String Lights box dieline</title>
<link rel="stylesheet" href="https://fonts.googleapis.com/css2?family=Dosis:wght@300;400;600;700&display=swap">
<style>
  :root{
    --box-black:#0b0b0c;
    --cut-line:#2a5f86;
    --amber:#f2962e;
    --sun-yellow:#f5b92e;
    --ink-white:#f4f2ee;
    --ink-grey:#bdbab4;
    --dim-blue:#1e8fd6;
    --page:#ffffff;
  }
  html,body{margin:0;padding:0;background:var(--page);width:1011px;height:1200px;overflow:hidden;}
  .dieline{position:absolute;left:0;top:333px;width:1011px;height:534px;display:block;}
  .dieline text{font-family:"Dosis",sans-serif;}
  .panel-fill{fill:var(--box-black);stroke:var(--cut-line);stroke-width:1.2;}
  .title-solar{fill:var(--ink-white);font-weight:400;letter-spacing:5px;}
  .title-outdoor{fill:var(--ink-white);font-weight:300;}
  .title-string{fill:var(--amber);font-weight:400;}
  .brand-name{fill:var(--ink-white);font-weight:400;}
  .brand-dot{fill:var(--sun-yellow);}
  .tagline{fill:var(--ink-grey);font-weight:300;}
  .bullet{fill:var(--ink-white);font-weight:400;}
  .bullet-lead{fill:var(--sun-yellow);font-weight:700;}
  .web-address{fill:var(--amber);font-weight:400;}
  .bulb-count{fill:var(--ink-white);font-weight:600;}
  .bulb-label{fill:var(--ink-grey);font-weight:400;}
  .amber-strip{fill:var(--amber);}
  .icon-disc{fill:var(--sun-yellow);}
  .icon-ink{fill:none;stroke:var(--box-black);stroke-width:2.4;stroke-linecap:round;}
  .icon-label{fill:var(--box-black);font-weight:700;}
  .dimension{fill:var(--dim-blue);font-weight:400;letter-spacing:1px;}
  .cert-mark{fill:var(--ink-white);}
</style>
</head>
<body>
<svg class="dieline" viewBox="20 830 1230 650" xmlns="http://www.w3.org/2000/svg">
  <defs>
    <linearGradient id="night-house" x1="0" y1="0" x2="1" y2="1">
      <stop offset="0" stop-color="#3a3328"/>
      <stop offset="0.45" stop-color="#b59a6c"/>
      <stop offset="0.7" stop-color="#2a241c"/>
      <stop offset="1" stop-color="#0d0d0e"/>
    </linearGradient>
    <linearGradient id="lid-facets" x1="0" y1="0" x2="1" y2="1">
      <stop offset="0" stop-color="#1b1b1d"/>
      <stop offset="0.5" stop-color="#0a0a0b"/>
      <stop offset="1" stop-color="#202022"/>
    </linearGradient>
  </defs>

  <text class="dimension" x="818" y="932" font-size="30" text-anchor="middle">230X180X115MM</text>

  <!-- top lid with tuck flap -->
  <path class="panel-fill" d="M68 1137 V885 Q68 848 100 846 H366 Q397 848 397 885 V1137 Z"/>
  <rect x="70" y="880" width="325" height="255" fill="url(#lid-facets)" role="img" aria-label="Dark faceted geometric background"/>

  <!-- top dust flaps -->
  <path class="panel-fill" d="M397 1137 V995 H605 Q615 995 620 1005 L652 1090 V1137 Z"/>
  <path class="panel-fill" d="M977 1137 V1090 L1010 1005 Q1015 995 1025 995 H1232 V1137 Z"/>
  <rect class="panel-fill" x="793" y="1117" width="42" height="20"/>

  <!-- bottom flaps -->
  <path class="panel-fill" d="M68 1303 H397 V1470 H285 V1430 H150 V1470 H68 Z"/>
  <path class="panel-fill" d="M397 1303 H652 L605 1400 H470 L397 1340 Z"/>
  <path class="panel-fill" d="M652 1303 H977 L910 1400 H715 Z"/>
  <path class="panel-fill" d="M977 1303 H1232 V1360 L1180 1470 H977 Z"/>

  <!-- glue flap and main band -->
  <path class="panel-fill" d="M30 1137 H68 V1303 H30 Z"/>
  <rect class="panel-fill" x="68" y="1137" width="1164" height="166"/>

  <!-- lid artwork (upside down, faces the front panel) -->
  <g class="lid-art" transform="rotate(180 232 1000)">
    <circle class="brand-dot" cx="172" cy="981" r="5"/>
    <text class="brand-name" x="184" y="988" font-size="20">Lumen Nook</text>
    <g class="feature-icon">
      <circle class="icon-disc" cx="158" cy="1035" r="32"/>
      <circle class="icon-ink" cx="158" cy="1030" r="7"/>
      <path class="icon-ink" d="M158 1016v-4M158 1044v4M144 1030h-4M172 1030h4M148 1020l-3-3M168 1040l3 3M168 1020l3-3M148 1040l-3 3"/>
      <text class="icon-label" x="158" y="1055" font-size="6.5" text-anchor="middle">Charges during</text>
      <text class="icon-label" x="158" y="1062" font-size="6.5" text-anchor="middle">the day</text>
    </g>
    <g class="feature-icon">
      <circle class="icon-disc" cx="232" cy="1035" r="32"/>
      <path class="icon-ink" d="M236 1018a13 13 0 1 0 8 22a10 10 0 0 1-8-22z"/>
      <text class="icon-label" x="232" y="1058" font-size="6.5" text-anchor="middle">Works at Dusk</text>
    </g>
    <g class="feature-icon">
      <circle class="icon-disc" cx="306" cy="1035" r="32"/>
      <path class="icon-ink" d="M296 1020v10a6 6 0 0 0 12 0v-10M300 1020v-5M304 1020v-5M302 1036v10M312 1044q6-14 14-10q-2 10-14 10z"/>
      <text class="icon-label" x="306" y="1058" font-size="6.5" text-anchor="middle">Green Energy</text>
    </g>
  </g>

  <!-- front panel -->
  <g class="panel-front">
    <rect x="69" y="1139" width="327" height="158" fill="url(#night-house)" role="img" aria-label="Night photo of a white house deck lit by warm string lights, hanging bulbs and a solar panel"/>
    <circle class="brand-dot" cx="82" cy="1163" r="3"/>
    <text class="brand-name" x="88" y="1166" font-size="9">Lumen Nook</text>
    <rect class="cert-mark" x="336" y="1146" width="14" height="12" rx="2"/>
    <circle cx="376" cy="1153" r="9" fill="none" stroke="var(--amber)" stroke-width="1.5"/>
    <text class="bulb-count" x="376" y="1157" font-size="10" text-anchor="middle">10</text>
    <text class="bulb-label" x="376" y="1168" font-size="4" text-anchor="middle">BULB SOLAR</text>
    <text class="title-solar" x="245" y="1234" font-size="11" text-anchor="middle">SOLAR</text>
    <text class="title-outdoor" x="245" y="1259" font-size="28" text-anchor="middle">OUTDOOR</text>
    <text class="title-string" x="245" y="1281" font-size="22" text-anchor="middle">STRING LIGHTS</text>
    <text class="tagline" x="245" y="1292" font-size="7" text-anchor="middle">Lorem Ipsum is simply dummy text of the printing.</text>
    <rect class="amber-strip" x="68" y="1297" width="329" height="5"/>
  </g>

  <!-- side info panel -->
  <g class="panel-side-info">
    <circle class="brand-dot" cx="412" cy="1200" r="3"/>
    <text class="brand-name" x="418" y="1203" font-size="9">Lumen Nook</text>
    <text class="title-solar" x="567" y="1163" font-size="10" text-anchor="middle">SOLAR</text>
    <text class="title-outdoor" x="565" y="1187" font-size="27" text-anchor="middle">OUTDOOR</text>
    <text class="title-string" x="565" y="1206" font-size="20" text-anchor="middle">STRING LIGHTS</text>
    <line x1="405" y1="1214" x2="645" y2="1214" stroke="#4a4a4a" stroke-width="1"/>
    <g font-size="6.2">
      <text class="bullet" x="412" y="1227"><tspan class="bullet-lead">✦ 10 LED</tspan> warm white light bulb string.</text>
      <text class="bullet" x="412" y="1238">✦ Waterproof connector for easy installation.</text>
      <text class="bullet" x="412" y="1249">✦ Total length <tspan class="bullet-lead">29.5 ft</tspan> / Lighted length <tspan class="bullet-lead">19.7 ft.</tspan></text>
      <text class="bullet" x="412" y="1260">✦ Creates pleasant ambient light perfect for Backyard,</text>
      <text class="bullet" x="418" y="1270">Patio, Party, Restaurant Wedding or other scenes.</text>
    </g>
    <text class="web-address" x="412" y="1286" font-size="8">www.lumennook-lights.com</text>
    <circle cx="610" cy="1243" r="18" fill="none" stroke="var(--amber)" stroke-width="1.6"/>
    <text class="bulb-count" x="610" y="1250" font-size="19" text-anchor="middle">10</text>
    <text class="bulb-label" x="608" y="1276" font-size="7.5" text-anchor="middle">BULB SOLAR</text>
    <text class="bulb-label" x="608" y="1285" font-size="7.5" text-anchor="middle">LIGHT STRING</text>
    <rect class="amber-strip" x="397" y="1297" width="255" height="5"/>
  </g>

  <!-- back panel -->
  <g class="panel-back">
    <rect x="653" y="1139" width="323" height="158" fill="url(#night-house)" role="img" aria-label="Night photo of a white house deck lit by warm string lights, hanging bulbs and a solar panel"/>
    <circle class="brand-dot" cx="666" cy="1163" r="3"/>
    <text class="brand-name" x="672" y="1166" font-size="9">Lumen Nook</text>
    <rect class="cert-mark" x="920" y="1146" width="14" height="12" rx="2"/>
    <circle cx="959" cy="1153" r="9" fill="none" stroke="var(--amber)" stroke-width="1.5"/>
    <text class="bulb-count" x="959" y="1157" font-size="10" text-anchor="middle">10</text>
    <text class="bulb-label" x="959" y="1168" font-size="4" text-anchor="middle">BULB SOLAR</text>
    <text class="title-solar" x="828" y="1234" font-size="11" text-anchor="middle">SOLAR</text>
    <text class="title-outdoor" x="828" y="1259" font-size="28" text-anchor="middle">OUTDOOR</text>
    <text class="title-string" x="828" y="1281" font-size="22" text-anchor="middle">STRING LIGHTS</text>
    <text class="tagline" x="828" y="1292" font-size="7" text-anchor="middle">Lorem Ipsum is simply dummy text of the printing.</text>
    <rect class="amber-strip" x="652" y="1297" width="325" height="5"/>
  </g>

  <!-- side technical panel -->
  <g class="panel-side-tech">
    <circle class="brand-dot" cx="993" cy="1200" r="3"/>
    <text class="brand-name" x="999" y="1203" font-size="9">Lumen Nook</text>
    <text class="title-solar" x="1150" y="1163" font-size="10" text-anchor="middle">SOLAR</text>
    <text class="title-outdoor" x="1148" y="1187" font-size="27" text-anchor="middle">OUTDOOR</text>
    <text class="title-string" x="1148" y="1206" font-size="20" text-anchor="middle">STRING LIGHTS</text>
    <g font-size="4.4">
      <text class="bullet" x="990" y="1226"><tspan class="bullet-lead">Safe and Convenient:</tspan> solar powered, no socket needed</text>
      <text class="bullet" x="994" y="1232">for use anywhere outdoors.</text>
      <text class="bullet" x="990" y="1241"><tspan class="bullet-lead">How it works:</tspan> the panel stores daylight energy and lights</text>
      <text class="bullet" x="994" y="1247">bulbs at dusk.</text>
      <text class="bullet" x="990" y="1256"><tspan class="bullet-lead">Where to place:</tspan> set the panel in full direct sun for best</text>
      <text class="bullet" x="994" y="1262">charging.</text>
      <text class="bullet" x="990" y="1271"><tspan class="bullet-lead">Ground Spike:</tspan> push the stake into soft soil until it is firmly in place.</text>
      <text class="bullet" x="990" y="1280"><tspan class="bullet-lead">Wall Mount:</tspan> fix the panel to a wall with two screws and</text>
      <text class="bullet" x="994" y="1286">adjust the angle.</text>
    </g>
    <rect class="amber-strip" x="977" y="1297" width="255" height="5"/>
  </g>
</svg>
</body>
</html>
```